Brightwell Chilled Supplies Stationery Design

Stationery Design

Thank you to all those who have submitted the logos. We have selected the logo for our new identity and we are now looking for stationery ideas.

The attached logo must be used in all stationery designs.

We require the following items of stationery:

1. Business Cards for 10 employees – Double Sided – All the card will have the same address:

7 – 31 Marlowby Lane, Kingston Upon Thames, Surrey, KT9 3QX, United Kingdom

Office phone number: +44 (0)208 631 7094

Freephone: 0800 113 4927

Fax: +44 (0)20 8392 6481

Website: www.brightwellchilled.example

The names on the cards and mobile numbers – will be given on selection of final design.

A few of the cards will have different emails but 5/6 card will have the same email address.

2. Letterhead A4 – same contact details as above – email address to be used info@brightwellchilled.example

3. Compliments Slip – same details as no.2

4. Envelope designs – with just the address, Freephone and Website.

Sizes Required: C4 – 324mm x 229mm – Windows and Regular

DL – 110mm x 220mm – Windows and Regular

5. A4 Ring Binder – Logo at the front and back and side; company name on the front and side of the binder (Brightwell Chilled Supplies); contact details at the back; same as number 2 above.

The ring binder will have food, drink and hygiene inserts inside and will act as a temporary brochure.

It may help with the design process to know we sell a range of frozen food products including chips, burgers, fish, frozen poultry items, vegetables, ice cream, desserts, bakery products, pies, pasties, onion rings, pizza toppings etc.

We also sell ambient products such as sauces, crisps such as dunmores, chocolates such as Threlfalls, Vorreau, Pell etc.

Drinks wise we sell branded products such as zesta fizz, korvo, brisa, glint, blue heron etc; As well as juices and mineral water.

We also sell hygiene products such as tissue paper, hand towels, and other washroom products, bleaches etc.

Our website doesn’t have the full range of products but gives you a good idea of what we do www.brightwellchilled.example

Please note we are looking for a classy, slick design so don’t worry about trying to add all the products on the binder design; these have just been given to assist with the design process.

We may add a slogan to the stationery but the final decision on this still has to be taken and the profile will be updated within the next 72 hours.

This project will only last a maximum of 10-14 days, we don’t want to drag it out like the logo so please only submit creative ideas; which have been given thought in terms of design, text and graphics.

Any questions, feel free to ask.

Thank you and we look forward to your designs.

Regards

Tariq Benmore

UPDATED FILES ATTACHED

I've uploaded an Adobe Illustrator CS2.ai file, and an EPS file of my new logo so you can get better clarity within your designs for this project

Thanks
Tariq

Hi

We have had various questions in respect of dimensions and budget; we have addressed both issues below by providing dimensions and we will be increasing the budget to $500 as soon as Sketch Hive let us know how we can increase; they have already been emailed.

In respect of the dimensions, we have had various answers but here are the most common sizes.

 

There are various sizes of lever arch A4 folders but the most common ones are below:

 

 

• Dimensions width 28.5cm, height 32cm,spine 9cm
• Dimensions (mm)H:315 x W:285
• Dimensions (mm) H:31cm x W:27cm

 

The most common thickness in the UK seems to be 70mm; so can we use this as a guide please.

 

 

Compliment Slip Sizes:

 

• Our Compliment Slips are DL in size. You should design your Compliment Slip to DL dimension but also add a 3mm bleed around each edge.

 

Trim Size – 99mm x 210mm

 

With Bleed – 105mm – 216mm

 

 

Business Cards:

 

Trim Size: 85mm x 55mm

 

With Bleed: 91mm x 61mm

 

 

We have extended the time frame and the budget on this so look forward to new designs.

 

I hope this helps and all the best for Christmas and 2010..

 

Regards

Tariq Benmore.

Hi Guys

Another important point to mention as each country has different rules...

In the Uk the postage stamps go in the top right hand corner of the envelope so we will have to have our logo company details etc in either the top left or the bottom of the envelope.

Also all envelopes must have at the back our return address:

Return Address:

Brightwell Chilled Supplies Ltd
7 - 31 Marlowby Lane
Kingston Upon Thames
Surrey
KT9 3QX

So we could even have the business logo, name and website address at the front and the address at the back.

Regards

Tariq

```html
<!DOCTYPE html>
<html lang="en">
<head>
<meta charset="utf-8">
<title>Brightwell Chilled Supplies – Stationery Set</title>
<link rel="stylesheet" href="https://fonts.googleapis.com/css2?family=Roboto+Condensed:wght@400;700&family=Arimo:wght@400;700&family=Great+Vibes&display=swap">
<style>
  :root{
    --paper:#ffffff;
    --canvas:#ffffff;
    --edge:#3a3a3a;
    --brand-red:#9a0b0b;
    --brand-blue:#1d1fa3;
    --brand-ice:#a9e3f4;
    --ink:#222222;
    --ink-soft:#6a6a6a;
    --rule:#b8b8c8;
  }
  *{box-sizing:border-box;margin:0;padding:0}
  html,body{width:1200px;height:667px;overflow:hidden;background:var(--canvas)}
  body{font-family:"Arimo",Arial,sans-serif;color:var(--ink)}
  .canvas{position:relative;width:1200px;height:667px;border:1px solid #bdbdbd;overflow:hidden}
  .piece{position:absolute;background:var(--paper);border:1px solid var(--edge);overflow:hidden}
  .emblem-area{position:absolute;border-radius:50%;
    background:radial-gradient(circle at 50% 50%, var(--paper) 0 8%, var(--brand-blue) 9% 38%, var(--brand-red) 39% 70%, var(--brand-ice) 71% 100%);
    opacity:.9}
  .brand-mark{position:absolute;display:flex;align-items:center;gap:2px;white-space:nowrap;
    font-family:"Roboto Condensed",Arial,sans-serif;font-weight:700;color:var(--ink)}
  .brand-mark .dot{display:inline-block;border-radius:50%;background:var(--brand-red)}
  .fine{position:absolute;font-family:"Arimo",Arial,sans-serif;color:var(--ink);white-space:nowrap;line-height:1.3}
  .fine b{font-weight:700}
  .rule-under{position:absolute;height:0;border-top:.6px solid var(--rule)}

  /* ring binder */
  .binder{position:absolute;left:31px;top:51px;width:607px;height:322px;overflow:hidden}
  .binder .panel{position:absolute;top:0;height:322px;background:var(--paper);border:1px solid var(--edge)}
  .binder-back{left:0;width:275px}
  .binder-spine{left:275px;width:55px}
  .binder-front{left:331px;width:276px}
  .binder-title{position:absolute;left:399px;top:17px;font-family:"Roboto Condensed",Arial,sans-serif;font-weight:400;font-size:14px;color:#3f3f3f;letter-spacing:.2px;white-space:nowrap}
  .spine-title{position:absolute;left:295px;top:136px;writing-mode:vertical-rl;font-family:"Roboto Condensed",Arial,sans-serif;font-weight:700;font-size:10px;color:#3f3f3f;white-space:nowrap}
  .binder-footer{position:absolute;left:0;width:275px;text-align:center;font-size:3.4px;color:var(--ink)}

  /* business cards & slip */
  .card{position:absolute;left:990px;width:176px;background:var(--paper);border:1px solid #9a9a9a;border-radius:6px;overflow:hidden;box-shadow:4px 4px 6px rgba(0,0,0,.22)}
  .card-link{position:absolute;font-size:5px;color:var(--brand-blue)}
  .connector{position:absolute;left:1077px;width:1px;background:var(--edge)}
  .card-name{position:absolute;right:90px;text-align:right;font-size:6px;line-height:1.25;white-space:nowrap}
  .card-name .main{color:var(--brand-red);font-weight:700}
  .card-name .role{color:var(--brand-blue);font-weight:700}
  .card-name .mail{color:var(--brand-red);font-size:5px}
  .card-detail{position:absolute;right:90px;text-align:right;font-size:4.9px;line-height:1.35;color:var(--brand-blue);white-space:nowrap}
  .card-divider{position:absolute;left:90px;top:10px;width:0;height:90px;border-left:.6px solid var(--rule)}
  .compliments{position:absolute;right:8px;top:6px;font-family:"Great Vibes",cursive;font-size:10px;color:var(--brand-red)}
</style>
</head>
<body>
<main class="canvas">

  <section class="binder" aria-label="Ring binder">
    <div class="panel binder-back">
      <div class="brand-mark" style="left:80px;top:286px;font-size:5.5px"><span class="dot" style="width:7px;height:7px"></span>Brightwell Chilled Supplies</div>
      <p class="fine binder-footer" style="top:301px">7 - 31 Marlowby Lane, Kingston Upon Thames, Surrey, KT9 3QX United Kingdom</p>
      <p class="fine binder-footer" style="top:307px"><b>Office #</b> +44 (0)208 631 7094 | <b>Freephone #</b> 0800 113 4927 | <b>Fax #</b> +44 (0)20 8392 6481 | <b>Email:</b> info@brightwellchilled.example | www.brightwellchilled.example</p>
    </div>
    <div class="panel binder-spine">
      <div class="brand-mark" style="left:3px;top:300px;font-size:3.4px"><span class="dot" style="width:6px;height:6px"></span>Brightwell Chilled Supplies</div>
    </div>
    <div class="panel binder-front">
      <div class="brand-mark" style="left:228px;top:300px;font-size:3.4px"><span class="dot" style="width:6px;height:6px"></span>Brightwell Chilled Supplies</div>
    </div>
    <div class="emblem-area" role="img" aria-label="Large decorative brand emblem in red, blue and ice blue" style="left:265px;top:1px;width:126px;height:126px"></div>
    <h1 class="binder-title">BRIGHTWELL CHILLED SUPPLIES</h1>
    <p class="spine-title">BRIGHTWELL CHILLED SUPPLIES</p>
  </section>

  <section class="piece" aria-label="DL envelope" style="left:33px;top:391px;width:260px;height:131px">
    <div class="emblem-area" role="img" aria-label="Decorative brand emblem" style="left:162px;top:44px;width:100px;height:100px"></div>
    <div class="brand-mark" style="left:6px;top:8px;font-size:5.5px"><span class="dot" style="width:8px;height:8px"></span>Brightwell Chilled Supplies</div>
    <div class="rule-under" style="left:6px;top:20px;width:44px"></div>
    <p class="fine" style="left:6px;top:23px;font-size:3px">7 - 31 Marlowby Lane<br>Kingston Upon Thames, Surrey<br>KT9 3QX United Kingdom</p>
    <p class="fine" style="left:6px;top:37px;font-size:3px"><b>Freephone #</b> 0800 113 4927<br>www.brightwellchilled.example</p>
  </section>

  <section class="piece" aria-label="C4 envelope" style="left:312px;top:390px;width:318px;height:225px">
    <div class="emblem-area" role="img" aria-label="Decorative brand emblem" style="left:236px;top:150px;width:90px;height:90px"></div>
    <div class="brand-mark" style="left:8px;top:8px;font-size:7px"><span class="dot" style="width:11px;height:11px"></span>Brightwell Chilled Supplies</div>
    <div class="rule-under" style="left:8px;top:24px;width:58px"></div>
    <p class="fine" style="left:10px;top:28px;font-size:3.4px">7 - 31 Marlowby Lane, Kingston<br>Upon Thames, Surrey<br>KT9 3QX United Kingdom</p>
    <p class="fine" style="left:10px;top:43px;font-size:3.4px"><b>Freephone #</b> 0800 113 4927<br>www.brightwellchilled.example</p>
  </section>

  <section class="piece" aria-label="A4 letterhead" style="left:660px;top:49px;width:419px;height:592px">
    <div class="emblem-area" role="img" aria-label="Large decorative brand emblem" style="left:-42px;top:-46px;width:186px;height:186px"></div>
    <div class="brand-mark" style="left:15px;top:493px;font-size:10px"><span class="dot" style="width:18px;height:18px;margin-right:2px"></span>Brightwell Chilled Supplies</div>
    <div class="rule-under" style="left:15px;top:518px;width:82px"></div>
    <p class="fine" style="left:15px;top:523px;font-size:5.5px;color:var(--ink-soft)">7 - 31 Marlowby Lane,<br>Kingston Upon Thames, Surrey<br>KT9 3QX United Kingdom</p>
    <p class="fine" style="left:15px;top:550px;font-size:5.5px;color:var(--ink-soft)"><b>Office #</b> +44 (0)208 631 7094<br><b>Freephone #</b> 0800 113 4927<br><b>Fax #</b> +44 (0)20 8392 6481<br><b>Email:</b> info@brightwellchilled.example</p>
  </section>

  <div class="connector" style="top:144px;height:420px"></div>
  <section class="card" aria-label="Business card, emblem side" style="top:43px;height:101px">
    <div class="emblem-area" role="img" aria-label="Decorative brand emblem" style="left:-2px;top:-6px;width:80px;height:80px"></div>
    <p class="fine card-link" style="right:6px;top:88px">www.brightwellchilled.example</p>
  </section>
  <section class="card" aria-label="Business card, centred emblem side" style="top:156px;height:101px">
    <div class="emblem-area" role="img" aria-label="Decorative brand emblem" style="left:53px;top:13px;width:70px;height:70px"></div>
    <p class="fine card-link" style="left:0;width:176px;text-align:center;top:88px">www.brightwellchilled.example</p>
  </section>
  <section class="card" aria-label="Business card, details side" style="top:270px;height:101px">
    <div class="card-name" style="top:9px"><span class="main">MAIN NAME</span><br><span class="role">Position Title</span><br><span class="mail">the.name@brightwellchilled.example</span></div>
    <p class="fine card-detail" style="top:46px">7 - 31 Marlowby Lane<br>Kingston Upon Thames, Surrey<br>KT9 3QX United Kingdom</p>
    <p class="fine card-detail" style="top:73px"><b>Office #</b> +44 (0)208 631 7094<br><b>Freephone #</b> 0800 113 4927<br><b>Fax #</b> +44 (0)20 8392 6481</p>
    <div class="card-divider"></div>
    <div class="brand-mark" style="left:94px;top:12px;font-size:5.2px"><span class="dot" style="width:12px;height:12px"></span>Brightwell Chilled</div>
  </section>

  <section class="card" aria-label="Compliments slip" style="top:384px;height:118px">
    <p class="compliments">With compliments</p>
    <div class="brand-mark" style="left:5px;top:64px;font-size:5px"><span class="dot" style="width:8px;height:8px"></span>Brightwell Chilled Supplies</div>
    <div class="rule-under" style="left:5px;top:75px;width:48px"></div>
    <p class="fine" style="left:6px;top:77px;font-size:2.6px;color:var(--ink-soft)">7 - 31 Marlowby Lane,<br>Kingston Upon Thames, Surrey<br>KT9 3QX United Kingdom</p>
    <p class="fine" style="left:6px;top:88px;font-size:2.6px;color:var(--ink-soft)"><b>Office #</b> +44 (0)208 631 7094<br><b>Freephone #</b> 0800 113 4927<br><b>Fax #</b> +44 (0)20 8392 6481<br><b>Email:</b> info@brightwellchilled.example<br>www.brightwellchilled.example</p>
  </section>

</main>
</body>
</html>
```